Private Investigator needs business card with an intelligent logo

Private Investigator needs uncluttered, intelligently designed business card with simple logo. Prefer one or two colour print only. Must convey serious approach with only basic information: Business Name, "Clearwater Inquiries"
Phone: 03 4196 5031 Email: info@clear-water.example.com.au Web: www.clear-water.example.com.au
Agents Name: Gavin Thornley Title: Investigator Mobile: 0417 263 594

Thank you all very much for your designs.  There was some really excellent ideas and the choice was very hard.  I sought opinions from a number of people about which was the best one and there were a number of different choices but eventually the majority went with one design from Rovelko.  Thank you especially to those designers that made some changes when I suggested them.

Thanks again for all your efforts and good luck with your design careers.  I will certainly use SketchMarket again with the great quality of designers that made submissions.

Regards  Gavin Thornley

```html
<!DOCTYPE html>
<html lang="en">
<head>
<meta charset="utf-8">
<title>Clearwater Inquiries – Business Card</title>
<link rel="stylesheet" href="https://fonts.googleapis.com/css2?family=PT+Sans:wght@400;700&display=swap">
<style>
  :root {
    --backdrop: #3b322e;
    --card: #f1f1f0;
    --card-edge: #e2e2e0;
    --ink-grey: #8e8e8e;
    --ink-dark: #3a3a3a;
    --print-light: #e4e4e3;
    --print-mid: #d6d6d5;
  }
  * { box-sizing: border-box; margin: 0; padding: 0; }
  html, body {
    width: 1200px; height: 716px; overflow: hidden;
    background: var(--backdrop);
    font-family: "PT Sans", sans-serif;
  }
  .canvas {
    position: relative; width: 1200px; height: 716px;
  }
  .card {
    position: absolute; top: 205px;
    width: 500px; height: 306px;
    background: var(--card);
    border: 1px solid var(--card-edge);
    overflow: hidden;
  }
  .card--back { left: 60px; }
  .card--front { left: 640px; }

  .fingerprint-area {
    position: absolute;
    border-radius: 46% 46% 40% 40%;
    background: radial-gradient(ellipse at 50% 45%, var(--print-mid) 0%, var(--print-light) 55%, rgba(228,228,227,0) 72%);
  }
  .card--back .fingerprint-area { left: 270px; top: 40px; width: 200px; height: 250px; }
  .card--front .fingerprint-area { left: -30px; top: -10px; width: 260px; height: 330px; }

  .agent {
    position: absolute; left: 30px; top: 26px;
  }
  .agent__name {
    font-weight: 700; font-size: 15px; letter-spacing: 0.5px;
    color: var(--ink-grey); text-transform: uppercase;
  }
  .agent__title {
    font-size: 13px; color: var(--ink-dark); margin-top: 1px;
  }

  .contacts {
    position: absolute; left: 30px; bottom: 30px;
    list-style: none;
  }
  .contacts li {
    display: flex; align-items: center; gap: 8px;
    font-size: 13px; line-height: 19px; color: var(--ink-dark);
  }
  .contacts svg { width: 11px; height: 11px; fill: var(--ink-grey); flex: none; }

  .brand {
    position: absolute; right: 34px; top: 118px;
    text-align: right;
    font-weight: 700; font-size: 44px; line-height: 40px;
    letter-spacing: -0.5px; text-transform: uppercase;
    color: var(--ink-grey);
  }
</style>
</head>
<body>
<main class="canvas">

  <section class="card card--back" aria-label="Card back with contact details">
    <div class="fingerprint-area" role="img" aria-label="Faint embossed fingerprint texture"></div>
    <div class="agent">
      <p class="agent__name">Gavin Thornley</p>
      <p class="agent__title">Investigator</p>
    </div>
    <ul class="contacts">
      <li>
        <svg viewBox="0 0 12 12" aria-hidden="true"><rect x="3" y="0.5" width="6" height="11" rx="1"/></svg>
        0417 263 594
      </li>
      <li>
        <svg viewBox="0 0 12 12" aria-hidden="true"><path d="M2.5 1 L4.5 1 L5.5 4 L4 5 C4.8 6.8 5.6 7.6 7 8 L8 6.5 L11 7.5 L11 9.5 C11 10.3 10.3 11 9.5 11 C5 11 1 7 1 2.5 C1 1.7 1.7 1 2.5 1 Z"/></svg>
        03 4196 5031
      </li>
      <li>
        <svg viewBox="0 0 12 12" aria-hidden="true"><path d="M0.5 2.5 H11.5 V9.5 H0.5 Z M0.5 2.5 L6 6.5 L11.5 2.5" stroke="#f1f1f0" stroke-width="0.8"/></svg>
        info@clear-water.example.com.au
      </li>
      <li>
        <svg viewBox="0 0 12 12" aria-hidden="true"><circle cx="6" cy="6" r="5.5"/><path d="M0.5 6 H11.5 M6 0.5 C3.5 3 3.5 9 6 11.5 M6 0.5 C8.5 3 8.5 9 6 11.5" stroke="#f1f1f0" stroke-width="0.7" fill="none"/></svg>
        www.clear-water.example.com.au
      </li>
    </ul>
  </section>

  <section class="card card--front" aria-label="Card front with business name">
    <div class="fingerprint-area" role="img" aria-label="Large embossed fingerprint texture"></div>
    <h1 class="brand">Clearwater<br>Inquiries</h1>
  </section>

</main>
</body>
</html>
```